Electrical contractor needs a flyer and business card

'Voltique - The Electrical Contractor' needs an a5 flyer designed which will showcase the work we undertake. We already have a logo - see attached
We operate in Devon and Cornwall in the UK in these 3 market sectors: Domestic, Commercial, Industrial.
The work we undertake is as follows:
House re-wires
New builds
RCD and consumer unit upgrades
Renovations
TV aerials & extra points
Data / phone / networking
Security and garden lighting
Extra external / internal sockets
Garage upgrades
LED and low energy lighting installs
We offer a free consumer unit and earthing check!
24 hour service.
prompt quality service with over 15 years experience
All our work is fully certified and guaranteed for a year
contact details:
Marcus Pelling
Owner
marcus@voltique-wiring.co.uk
www.voltique-wiring.co.uk
m: 07938661207
t: 01392 586 031
Servicing Devon & Cornwall
We also need a business card designed
many thanks
Raf
Target Market(s)
Domestic, Commercial, Industrial.
Industry/Entity Type
Contractor
Font styles to use
Other font styles liked:
- eurostile extended
Look and feel

```html
<!DOCTYPE html>
<html lang="en">
<head>
<meta charset="utf-8">
<title>Voltique - The Electrical Contractor flyer</title>
<link rel="stylesheet" href="https://fonts.googleapis.com/css2?family=Arimo:wght@400;700&display=swap">
<style>
:root{
  --teal:#97d0cb;
  --ink:#454545;
  --dark:#4a4a4a;
  --white:#ffffff;
}
html,body{margin:0;padding:0;overflow:hidden;background:var(--white);}
.canvas{position:relative;width:1200px;height:900px;background:var(--white);font-family:'Arimo',Arial,sans-serif;color:var(--ink);}
.flyer{position:absolute;left:319px;top:63px;width:576px;height:792px;background:var(--white);}
.band{position:absolute;left:0;width:576px;height:16px;background:var(--teal);}
.band-top{top:0;}
.band-bottom{top:102px;}
.brand{position:absolute;left:0;top:16px;width:576px;height:86px;display:flex;align-items:center;justify-content:center;}
.brand-name{font-family:'Arimo',Arial,sans-serif;font-weight:700;font-size:26px;color:var(--ink);margin:0;}
.headline{position:absolute;left:0;top:127px;width:556px;text-align:center;font-weight:700;font-size:35px;line-height:43px;margin:0;color:var(--ink);}
.panel{position:absolute;top:274px;height:370px;background:var(--teal);border-radius:10px;text-align:center;font-weight:700;}
.panel-services{left:10px;width:265px;}
.panel-areas{left:301px;width:266px;}
.panel-title{font-size:22px;margin:12px 0 20px;}
.service-list{list-style:none;margin:0;padding:0 18px;font-size:17px;line-height:21.6px;}
.areas-title{font-size:22px;line-height:29px;margin:17px 0 0;}
.areas-text{font-size:22px;line-height:29px;margin:0;}
.areas-country{color:var(--white);font-size:26px;margin:5px 0 26px;}
.sector-title{font-size:26px;margin:0 0 38px;}
.sector-list{list-style:none;margin:0;padding:0;font-size:17px;line-height:22px;}
.footer{position:absolute;left:0;top:660px;width:576px;height:132px;background:var(--dark);color:var(--white);font-weight:700;}
.footer-offer{position:absolute;left:18px;top:22px;width:180px;margin:0;text-align:center;font-size:23px;line-height:29px;}
.footer-hours{position:absolute;right:18px;top:2px;width:100px;margin:0;text-align:center;font-size:22px;line-height:28px;}
.footer-hours span{display:block;font-size:66px;line-height:70px;}
</style>
</head>
<body>
<div class="canvas">
  <article class="flyer">
    <div class="band band-top"></div>
    <header class="brand">
      <p class="brand-name">Voltique - The Electrical Contractor</p>
    </header>
    <div class="band band-bottom"></div>
    <h1 class="headline">15+ YEARS EXPERIENCE<br>WITH<br>QUALITY SERVICE</h1>
    <section class="panel panel-services">
      <h2 class="panel-title">SERVICES</h2>
      <ul class="service-list">
        <li>House re-wires</li>
        <li>New builds</li>
        <li>RCD and consumer unit upgrades</li>
        <li>Renovations</li>
        <li>TV aerials &amp; extra points</li>
        <li>Data / phone / networking</li>
        <li>Security and garden lighting</li>
        <li>Extra external / internal sockets</li>
        <li>Garage upgrades</li>
        <li>LED and low energy lighting installs</li>
      </ul>
    </section>
    <section class="panel panel-areas">
      <h2 class="areas-title">OUR OPERATING<br>AREAS</h2>
      <p class="areas-text">We operate in Devon<br>and Cornwall in the</p>
      <p class="areas-country">UK</p>
      <h2 class="sector-title">Market sector</h2>
      <ul class="sector-list">
        <li>Domestic</li>
        <li>Commercial</li>
        <li>Industrial</li>
      </ul>
    </section>
    <footer class="footer">
      <p class="footer-offer">Free consumer unit &amp; earth checking</p>
      <p class="footer-hours"><span>24</span>Hour Service</p>
    </footer>
  </article>
</div>
</body>
</html>
```